TK Drafting

Simple Design - Logo is done (from this site). Logo on one side - Back Side an image or outline of a house blue print - My name, phone, email, website url. Prefer the traditional Architectural style of letters -

Target Market(s)

Customers who need a floor plan redesigned for renovations or realtors who want a floor plan for marketing their listings

Industry/Entity Type

Architecture

Contact Information for Business Card

Colby Faust - Name
415-362-8840 - Phone
tkdraftingco@mailpost.example
www.tkdraftingco.example

Font styles to use
Other font styles liked:
• Architecture writing -

Colors
0555a3
3276b5
85acd3

Requirements
Must have
• Logo that is attached. I like an indigo blue color for the background or a royal blue - gray logo OR - white and clean with the logo on one side and the same color gray lettering on the other side
Nice to have
• some sort of image that shows a residential blue print. It may not be possible on this small of a card though.
Should not have
• Nothing cartoonish.

```html
<!DOCTYPE html>
<html lang="en">
<head>
<meta charset="UTF-8">
<title>TK Drafting – Business Card</title>
<link href="https://fonts.googleapis.com/css2?family=Roboto:wght@400;500;700&display=swap" rel="stylesheet">
<style>
  :root {
    --backdrop: #3b3b3d;
    --card-blue: #0b3a80;
    --card-blue-deep: #082c66;
    --ink-light: #c9d3e6;
    --ink-soft: #aebbd6;
    --card-shadow: rgba(0, 0, 0, 0.55);
  }
  * { margin: 0; padding: 0; box-sizing: border-box; }
  html, body {
    width: 1200px;
    height: 900px;
    overflow: hidden;
    background: var(--backdrop);
    font-family: "Roboto", Arial, sans-serif;
  }
  .stage {
    width: 1200px;
    height: 900px;
    display: flex;
    flex-direction: column;
    align-items: center;
    justify-content: center;
    gap: 44px;
  }
  .card {
    width: 630px;
    height: 360px;
    border-radius: 6px;
    background: linear-gradient(150deg, var(--card-blue) 0%, var(--card-blue-deep) 100%);
    box-shadow: 0 18px 40px var(--card-shadow);
    position: relative;
    color: var(--ink-light);
  }

  /* Front face */
  .card--front {
    display: flex;
    align-items: center;
    justify-content: center;
  }
  .brand {
    display: flex;
    align-items: center;
    gap: 16px;
  }
  .brand__mark {
    width: 30px;
    height: 30px;
    background: var(--ink-light);
  }
  .brand__name {
    font-size: 46px;
    font-weight: 500;
    letter-spacing: 3px;
    color: var(--ink-light);
  }

  /* Back face */
  .card--back {
    display: flex;
    align-items: center;
    padding: 0 50px 0 48px;
  }
  .card--back .brand { gap: 10px; }
  .card--back .brand__mark { width: 18px; height: 18px; }
  .card--back .brand__name { font-size: 28px; letter-spacing: 2px; }

  .divider {
    width: 2px;
    height: 190px;
    margin: 0 34px 0 34px;
    display: flex;
    flex-direction: column;
    gap: 14px;
  }
  .divider__short { height: 26px; background: var(--ink-soft); }
  .divider__long { flex: 1; background: var(--ink-soft); }

  .contact__name {
    font-size: 24px;
    font-weight: 700;
    letter-spacing: 0.5px;
    color: var(--ink-light);
    text-transform: uppercase;
  }
  .contact__role {
    font-size: 16px;
    font-weight: 500;
    color: var(--ink-soft);
    margin-bottom: 18px;
  }
  .contact__list { list-style: none; }
  .contact__item {
    display: flex;
    align-items: center;
    gap: 10px;
    font-size: 16px;
    line-height: 26px;
    color: var(--ink-light);
  }
  .contact__icon {
    width: 16px;
    height: 16px;
    flex: none;
  }
</style>
</head>
<body>
<main class="stage">

  <section class="card card--front" aria-label="Card front">
    <div class="brand">
      <span class="brand__mark"></span>
      <span class="brand__name">TK Drafting</span>
    </div>
  </section>

  <section class="card card--back" aria-label="Card back">
    <div class="brand">
      <span class="brand__mark"></span>
      <span class="brand__name">TK Drafting</span>
    </div>

    <div class="divider" aria-hidden="true">
      <span class="divider__short"></span>
      <span class="divider__long"></span>
    </div>

    <div class="contact">
      <p class="contact__name">Colby Faust</p>
      <p class="contact__role">Director</p>
      <ul class="contact__list">
        <li class="contact__item">
          <svg class="contact__icon" viewBox="0 0 16 16" aria-hidden="true">
            <path d="M3.5 1.5 L6 1.8 L6.8 5 L5.2 6.2 C6 8 7.8 9.8 9.8 10.8 L11 9.2 L14.2 10 L14.5 12.5 C14.5 13.6 13.6 14.5 12.5 14.5 C6.5 14.2 1.8 9.5 1.5 3.5 C1.5 2.4 2.4 1.5 3.5 1.5 Z" fill="#c9d3e6"/>
          </svg>
          415-362-8840
        </li>
        <li class="contact__item">
          <svg class="contact__icon" viewBox="0 0 16 16" aria-hidden="true">
            <rect x="1" y="3" width="14" height="10" rx="1" fill="#c9d3e6"/>
            <path d="M1.5 3.5 L8 9 L14.5 3.5" fill="none" stroke="#0b3a80" stroke-width="1.3"/>
          </svg>
          tkdraftingco@mailpost.example
        </li>
        <li class="contact__item">
          <svg class="contact__icon" viewBox="0 0 16 16" aria-hidden="true">
            <g fill="none" stroke="#c9d3e6" stroke-width="1.3">
              <circle cx="8" cy="8" r="6.5"/>
              <ellipse cx="8" cy="8" rx="2.8" ry="6.5"/>
              <line x1="1.5" y1="8" x2="14.5" y2="8"/>
            </g>
          </svg>
          www.tkdraftingco.example
        </li>
      </ul>
    </div>
  </section>

</main>
</body>
</html>
```